Design of an attractive membership brochure/membership card for an Electrical Business

Hi, we are an electrical business based in Sydney, Australia.

Our design's aim is to attract and target new customers into using our business as a repeat for anything electrical in their home. We would be handing this out to them after a job is completed and they're happy with the service.
We're thinking of a brochure, possibly additional membership cards with personalized number ID's for each client.

Open to ideas, but some of the things we want to include on our brochure are perks of why the client should sign up with us as a lifetime client
- Discounted emergency call out fees outside of normal hours
- Lifetime membership price, one time payment
- Exclusive 10% member discount on all future jobs
- Priority on any during business hour jobs or emergencies

If any other questions please don't hesitate to reach out.
We've attached our logo for reference for the mock designs.
Our website
https://brightwirehaus.com.au/

```html
<!DOCTYPE html>
<html lang="en">
<head>
<meta charset="utf-8">
<title>Brightwire Haus – Membership Flyer and Cards</title>
<link href="https://fonts.googleapis.com/css2?family=Audiowide&family=Poppins:wght@400;500;600;700;800&display=swap" rel="stylesheet">
<style>
:root{
  --red:#ee3524;
  --black:#0b0b0b;
  --white:#ffffff;
  --grey-bg:#c4c4c4;
  --ink:#111111;
  --rule:#d8d8d8;
  --gold-1:#f7e27a;
  --gold-2:#c99a2b;
  --gold-3:#8e6a14;
}
*{margin:0;padding:0;box-sizing:border-box}
html,body{width:834px;height:1200px;overflow:hidden}
body{background:var(--grey-bg);font-family:'Poppins',sans-serif;color:var(--ink);position:relative}

.flyer{position:absolute;left:98px;top:83px;width:638px;height:826px;background:var(--white);overflow:hidden;box-shadow:0 8px 20px rgba(0,0,0,.25)}
.flyer-art{position:absolute;left:0;top:0}

.brand{position:absolute;font-family:'Poppins',sans-serif;font-weight:700;color:var(--red);display:flex;align-items:center;gap:7px;letter-spacing:.5px;white-space:nowrap}
.brand-dot{width:12px;height:12px;background:var(--red);border-radius:50%}
.flyer .brand{left:44px;top:52px;font-size:24px;line-height:1}

.hero{position:absolute;left:0;top:109px;width:364px;height:184px;background:radial-gradient(circle at 75% 70%,#2b2b2b 0%,#111 55%,#050505 100%)}
.hero-kicker{position:absolute;left:42px;top:14px;font-family:'Audiowide',sans-serif;color:var(--white);font-size:18px;letter-spacing:.5px}
.hero-title{position:absolute;left:40px;top:34px;font-family:'Audiowide',sans-serif;color:var(--red);font-size:38px;line-height:36px}
.hero-rule{position:absolute;left:42px;top:114px;width:274px;height:1px;background:var(--white)}
.hero-rule::before{content:"";position:absolute;left:0;top:-1px;width:44px;height:3px;background:var(--white)}
.hero-sub{position:absolute;left:42px;top:125px;color:var(--white);font-size:17px;font-weight:500;line-height:20px}

.section-title{position:absolute;left:42px;font-size:19px;font-weight:700;line-height:1}
.section-title span{color:var(--red)}
.about-title{top:308px}
.about-text{position:absolute;left:42px;top:332px;width:272px;font-size:8.4px;line-height:10px}
.service-title{top:400px}

.service-list{position:absolute;left:42px;top:425px;width:270px;list-style:none}
.service-list li{position:relative;height:19.7px;line-height:18px;padding-left:15px;font-size:9.6px;font-weight:500;border-bottom:1px solid var(--rule)}
.service-list li:last-child{border-bottom:none}
.service-list li::before{content:"";position:absolute;left:3px;top:5px;width:7px;height:7px;border-radius:50%;background:var(--red)}
.service-list li::after{content:"";position:absolute;left:5px;top:7px;width:3px;height:1.5px;border-left:1px solid #fff;border-bottom:1px solid #fff;transform:rotate(-45deg)}

.badge-text{position:absolute;left:336px;top:335px;width:116px;text-align:center;font-size:11px;line-height:13.5px;color:#2a2000}
.badge-text b{font-weight:700}

.pitch{position:absolute;left:330px;top:425px;font-size:15.5px;font-weight:500;line-height:20px;text-transform:uppercase}
.pitch strong{display:block;font-weight:800;font-size:19.5px;line-height:20px}
.pitch .accent{color:var(--red)}

.perks{position:absolute;left:333px;top:494px;width:261px}
.perk{height:42px;margin-bottom:8px;border-radius:8px;display:flex;align-items:center;color:var(--white);font-size:10.2px;font-weight:600;line-height:12px;box-shadow:0 3px 5px rgba(0,0,0,.3)}
.perk-red{background:var(--red)}
.perk-black{background:var(--black)}
.perk-icon{width:58px;display:flex;justify-content:center}
.perk-text{flex:1;padding-right:40px}

.footer{position:absolute;left:0;top:738px;width:638px;height:88px;background:var(--black)}
.cta{position:absolute;left:81px;top:718px;width:476px;height:37px;border-radius:19px;background:var(--red);border:2px solid var(--white);color:var(--white);font-weight:700;font-size:17.5px;display:flex;align-items:center;justify-content:center;letter-spacing:.2px}
.contacts{position:absolute;display:flex;align-items:center;color:var(--white);white-space:nowrap}
.contacts .item{display:flex;align-items:center;gap:5px}
.flyer .contacts{left:45px;top:769px;font-size:12.6px;font-weight:500;gap:18px}

.card{position:absolute;top:941px;width:309px;height:175px;background:var(--black);box-shadow:0 8px 18px rgba(0,0,0,.3);overflow:hidden}
.card-vip{left:97px}
.card-member{left:428px}
.card-vip .brand{left:0;right:0;top:40px;justify-content:center;font-size:26px}
.vip-band{position:absolute;left:0;top:113px;width:309px;height:23px;background:linear-gradient(90deg,var(--gold-3),var(--gold-2) 30%,var(--gold-1) 55%,var(--gold-2) 80%,var(--gold-3));display:flex;align-items:center;justify-content:center;font-family:'Audiowide',sans-serif;font-size:20px;letter-spacing:4px;color:var(--black)}
.vip-sub{position:absolute;left:0;right:0;top:138px;text-align:center;font-family:'Audiowide',sans-serif;font-size:11px;letter-spacing:4.5px;color:var(--gold-2)}

.member-title{position:absolute;left:11px;top:38px;font-family:'Audiowide',sans-serif;font-size:15px;color:var(--gold-2);background:linear-gradient(90deg,var(--gold-2),var(--gold-1),var(--gold-2));-webkit-background-clip:text;background-clip:text;-webkit-text-fill-color:transparent}
.card-member .brand{right:11px;top:40px;font-size:8.6px;gap:3px;letter-spacing:.2px;line-height:1}
.card-member .brand-dot{width:6px;height:6px}
.field{position:absolute;height:19px;background:var(--white)}
.field-name{left:11px;top:63px;width:287px}
.field-number{left:11px;top:95px;width:137px}
.field-valid{left:157px;top:95px;width:78px}
.field-label{position:absolute;color:var(--white);font-size:6px;font-weight:600;letter-spacing:.6px}
.label-name{left:11px;top:85px}
.label-number{left:11px;top:117px}
.label-valid{left:157px;top:117px}
.card-member .contacts{left:10px;top:139px;font-size:6.6px;gap:9px}
.card-member .contacts .item{gap:3px}
</style>
</head>
<body>

<section class="flyer">
  <svg class="flyer-art" width="638" height="826" viewBox="0 0 638 826">
    <defs>
      <linearGradient id="roomTone" x1="0" y1="0" x2="0.6" y2="1">
        <stop offset="0" stop-color="#ecebe8"/>
        <stop offset="0.45" stop-color="#a8a29a"/>
        <stop offset="1" stop-color="#4a4038"/>
      </linearGradient>
      <radialGradient id="goldTone" cx="0.4" cy="0.35" r="0.7">
        <stop offset="0" stop-color="#fff3a8"/>
        <stop offset="0.55" stop-color="#e6c24a"/>
        <stop offset="1" stop-color="#a47a18"/>
      </radialGradient>
    </defs>
    <path d="M386,0 C364,30 360,70 360,110 L360,260 C360,330 430,388 525,390 C580,390 620,352 638,312 L638,0 Z" fill="#ee3524"/>
    <path d="M400,0 C380,30 374,70 374,110 L374,250 C374,322 432,372 515,374 C575,374 615,342 638,297 L638,0 Z" fill="url(#roomTone)" role="img" aria-label="Photo of a modern kitchen with pendant lights, island bench and stools"/>
    <rect x="503" y="368" width="20" height="30" fill="#ffffff"/>
    <g transform="translate(394,362)" fill="url(#goldTone)">
      <rect x="-46" y="-46" width="92" height="92"/>
      <rect x="-46" y="-46" width="92" height="92" transform="rotate(22.5)"/>
      <rect x="-46" y="-46" width="92" height="92" transform="rotate(45)"/>
      <rect x="-46" y="-46" width="92" height="92" transform="rotate(67.5)"/>
      <circle r="52"/>
    </g>
  </svg>

  <div class="brand"><span class="brand-dot"></span>BRIGHTWIRE HAUS</div>

  <header class="hero">
    <p class="hero-kicker">SYDNEY-BASED</p>
    <h1 class="hero-title">ELECTRICAL<br>BUSINESS</h1>
    <div class="hero-rule"></div>
    <p class="hero-sub">Specialising in electrical<br>maintenance</p>
  </header>

  <h2 class="section-title about-title">About <span>Us</span></h2>
  <p class="about-text">We work for residential, commercial, strata and real estate clients. It began with two mates with a strong desire to change the image of tradies and provide exceptional service. As a team of electricians based in the Inner West of Sydney, we understand the need of everyday people struggling to find good, reliable and trustworthy electricians.</p>

  <h2 class="section-title service-title">Our <span>service</span></h2>
  <ul class="service-list">
    <li>Lighting layout design and installations</li>
    <li>Emergency services</li>
    <li>Smoke alarm installations and testing</li>
    <li>Level 2 electrician</li>
    <li>Ceiling fans, exhaust fans &amp; general ventilation</li>
    <li>Powerpoint installations or repair</li>
    <li>Electrical fault finding</li>
    <li>Surge protection</li>
    <li>Switchboard upgrade and repairs</li>
    <li>Hot water diagnosis &amp; repair</li>
    <li>Tv antenna installation &amp; diagnostics</li>
    <li>Data &amp; nbn</li>
    <li>Renovation and fitouts</li>
    <li>Appliance installation</li>
  </ul>

  <p class="badge-text">CUSTOMER<br>SATISFACTION IS<br><b>OUR HIGHEST<br>PRIORITY</b></p>

  <h2 class="pitch">Are you looking for<strong class="accent">Electricians based</strong><strong>in Sydney?</strong></h2>

  <div class="perks">
    <div class="perk perk-red">
      <div class="perk-icon"><svg width="26" height="26" viewBox="0 0 24 24" fill="none" stroke="#fff" stroke-width="1.8" stroke-linecap="round" stroke-linejoin="round"><path d="M5 3h3l2 5-2.5 1.5a11 11 0 0 0 6 6L15 13l5 2v3a2 2 0 0 1-2 2A16 16 0 0 1 3 5a2 2 0 0 1 2-2z"/><path d="M15 3a6 6 0 0 1 6 6M15 6.5a2.5 2.5 0 0 1 2.5 2.5"/></svg></div>
      <p class="perk-text">Discounted emergency call out fees outside of normal hours</p>
    </div>
    <div class="perk perk-black">
      <div class="perk-icon"><svg width="26" height="28" viewBox="0 0 24 26" fill="none" stroke="#fff" stroke-width="1.8" stroke-linejoin="round"><circle cx="12" cy="10" r="8"/><circle cx="12" cy="8" r="2.2"/><path d="M8.5 14a3.5 3.5 0 0 1 7 0z"/><path d="M7 16.5 4.5 23l3-1 1.5 2.5 2-5M17 16.5l2.5 6.5-3-1-1.5 2.5-2-5"/></svg></div>
      <p class="perk-text">Lifetime membership price, one time payment</p>
    </div>
    <div class="perk perk-red">
      <div class="perk-icon"><svg width="28" height="28" viewBox="0 0 24 24"><circle cx="12" cy="12" r="10.5" fill="#fff"/><g stroke="#ee3524" stroke-width="1.8" fill="none" stroke-linecap="round"><path d="M8 16 16 8"/><circle cx="8.8" cy="8.8" r="1.6"/><circle cx="15.2" cy="15.2" r="1.6"/></g></svg></div>
      <p class="perk-text">Exclusive 10% member discount on all future jobs</p>
    </div>
    <div class="perk perk-black">
      <div class="perk-icon"><svg width="28" height="28" viewBox="0 0 24 24" fill="#fff"><circle cx="10" cy="6" r="4"/><path d="M2 20c0-5 3.5-8 8-8 2 0 3.4.5 4.5 1.3V20z"/><rect x="14" y="14" width="9" height="7" rx="1" stroke="#0b0b0b" stroke-width=".8"/><path d="M14 14.5l4.5 3.5 4.5-3.5" fill="none" stroke="#0b0b0b" stroke-width=".9"/></svg></div>
      <p class="perk-text">Priority on any during business hour jobs or emergencies</p>
    </div>
  </div>

  <footer class="footer"></footer>
  <div class="cta">CALL NOW AND GET A FREE QUOTATION TODAY!</div>
  <div class="contacts">
    <span class="item"><svg width="16" height="16" viewBox="0 0 24 24" fill="#ee3524"><path d="M5 3h3l2 5-2.5 1.5a11 11 0 0 0 6 6L15 13l5 2v3a2 2 0 0 1-2 2A16 16 0 0 1 3 5a2 2 0 0 1 2-2z"/></svg>0400 555 218</span>
    <span class="item"><svg width="14" height="14" viewBox="0 0 24 24" fill="none" stroke="#ee3524" stroke-width="2"><circle cx="12" cy="12" r="10"/><path d="M2 12h20M12 2c3 3 3 17 0 20M12 2c-3 3-3 17 0 20"/></svg>www.brightwirehaus.com.au</span>
    <span class="item"><svg width="15" height="12" viewBox="0 0 24 18" fill="#ee3524"><rect width="24" height="18" rx="1"/><path d="M1 1l11 9 11-9" fill="none" stroke="#0b0b0b" stroke-width="1.6"/></svg>services@brightwirehaus.com.au</span>
  </div>
</section>

<section class="card card-vip">
  <div class="brand"><span class="brand-dot"></span>BRIGHTWIRE HAUS</div>
  <div class="vip-band">VIP CARD</div>
  <p class="vip-sub">MEMBERS ONLY</p>
</section>

<section class="card card-member">
  <h2 class="member-title">MEMBERSHIP CARD</h2>
  <div class="brand"><span class="brand-dot"></span>BRIGHTWIRE HAUS</div>
  <div class="field field-name"></div>
  <span class="field-label label-name">NAME</span>
  <div class="field field-number"></div>
  <div class="field field-valid"></div>
  <span class="field-label label-number">MEMBERSHIP NO.</span>
  <span class="field-label label-valid">VALID TILL.</span>
  <div class="contacts">
    <span class="item"><svg width="8" height="8" viewBox="0 0 24 24" fill="#ee3524"><path d="M5 3h3l2 5-2.5 1.5a11 11 0 0 0 6 6L15 13l5 2v3a2 2 0 0 1-2 2A16 16 0 0 1 3 5a2 2 0 0 1 2-2z"/></svg>0400 555 218</span>
    <span class="item"><svg width="7" height="7" viewBox="0 0 24 24" fill="none" stroke="#ee3524" stroke-width="2.5"><circle cx="12" cy="12" r="10"/><path d="M2 12h20M12 2c3 3 3 17 0 20M12 2c-3 3-3 17 0 20"/></svg>www.brightwirehaus.com.au</span>
    <span class="item"><svg width="8" height="6" viewBox="0 0 24 18" fill="#ee3524"><rect width="24" height="18" rx="1"/><path d="M1 1l11 9 11-9" fill="none" stroke="#0b0b0b" stroke-width="2"/></svg>services@brightwirehaus.com.au</span>
  </div>
</section>

</body>
</html>
```